Design a New Business Card for Our Company

We are looking for fresh, unique, and a modern business card that reflects our roots as digital marketing agency focused on SEM.

Industry/Entity Type

Marketing

Contact Information for Business Card

looking for very unique out of the box designs. clean and modern that compliments our logo

Requirements
Must have
• colors should match our logo
• Front should have name, address, email, and phone/fax of the person, phone/fax are the same number
• back should have our url

```html
<!DOCTYPE html>
<html lang="en">
<head>
<meta charset="utf-8">
<title>Brightpath Solutions – Business Card</title>
<link href="https://fonts.googleapis.com/css2?family=Lato:wght@400;700;900&display=swap" rel="stylesheet">
<style>
  :root {
    --stage: #2b2b2b;
    --card: #f4f4f4;
    --card-edge: #e2e2e2;
    --ink: #6b6b6b;
    --ink-dark: #555555;
    --brand-blue: #3d7cc4;
    --rule: #8a8a8a;
    --pattern-a: #e4e4e4;
    --pattern-b: #f2f2f2;
  }
  * { box-sizing: border-box; margin: 0; padding: 0; }
  html, body { width: 1200px; height: 997px; overflow: hidden; }
  body {
    background: var(--stage);
    font-family: "Lato", Arial, sans-serif;
    position: relative;
  }
  .card {
    position: absolute;
    width: 600px;
    height: 343px;
    border-radius: 22px;
    background: linear-gradient(160deg, #fbfbfb 0%, var(--card) 60%, var(--card-edge) 100%);
    box-shadow: 0 18px 40px rgba(0,0,0,0.55);
    overflow: hidden;
  }
  .card--back { left: 90px; top: 90px; }
  .card--front { left: 510px; top: 500px; }

  /* Back side */
  .type-pattern {
    position: absolute;
    left: 0; top: 0;
    width: 100%; height: 100%;
    background: linear-gradient(120deg, var(--pattern-a) 0%, var(--pattern-b) 55%, var(--pattern-a) 100%);
  }
  .brand {
    display: flex;
    align-items: center;
    gap: 12px;
    font-weight: 900;
    color: var(--ink);
    white-space: nowrap;
  }
  .brand__dot {
    border-radius: 50%;
    background: var(--brand-blue);
    flex: none;
  }
  .card--back .brand {
    position: absolute;
    left: 70px; top: 120px;
    font-size: 44px;
    letter-spacing: -0.5px;
  }
  .card--back .brand__dot { width: 40px; height: 40px; }
  .tagline {
    position: absolute;
    left: 122px;
    font-size: 18px;
  }
  .tagline--accent { top: 200px; color: var(--brand-blue); }
  .tagline--main { top: 226px; color: var(--ink-dark); font-size: 19px; }

  /* Front side */
  .card--front .brand {
    position: absolute;
    right: 36px; top: 34px;
    font-size: 26px;
    gap: 8px;
  }
  .card--front .brand__dot { width: 22px; height: 22px; }
  .front-rule {
    position: absolute;
    height: 1.5px;
    background: var(--rule);
  }
  .front-rule--top { left: 250px; right: 110px; top: 110px; }
  .front-rule--name { left: 250px; right: 110px; top: 190px; }
  .dot-field {
    position: absolute;
    right: 0; top: 130px;
    width: 120px; height: 150px;
    background: radial-gradient(circle at 70% 50%, #d8dde4 0%, rgba(244,244,244,0) 70%);
  }
  .person {
    position: absolute;
    left: 36px; top: 160px;
  }
  .person__name {
    font-size: 22px;
    font-weight: 900;
    color: var(--ink);
  }
  .person__role {
    font-size: 13px;
    font-weight: 700;
    color: var(--brand-blue);
    letter-spacing: 0.5px;
    margin-top: 1px;
  }
  .contact {
    position: absolute;
    left: 36px; top: 232px;
    list-style: none;
    font-size: 16px;
    color: var(--ink);
    line-height: 21px;
  }
  .contact li { display: flex; align-items: flex-start; gap: 12px; }
  .contact__icon { flex: none; width: 16px; height: 16px; margin-top: 2px; }
  .contact__text { display: block; }
  .website {
    position: absolute;
    right: 40px; bottom: 34px;
    font-size: 15px;
    font-weight: 700;
    color: var(--brand-blue);
  }
</style>
</head>
<body>

  <section class="card card--back" aria-label="Business card back">
    <div class="type-pattern" role="img" aria-label="Faint large typographic pattern of marketing words such as SEM, marketing, engine and advertising"></div>
    <div class="brand"><span class="brand__dot"></span>Brightpath Solutions</div>
    <p class="tagline tagline--accent">Powering online profits since 2006</p>
    <p class="tagline tagline--main">Digital marketing agency focused on SEM</p>
  </section>

  <section class="card card--front" aria-label="Business card front">
    <div class="brand"><span class="brand__dot"></span>Brightpath Solutions</div>
    <div class="front-rule front-rule--top"></div>
    <div class="dot-field" role="img" aria-label="Soft decorative dot cluster in grey and blue"></div>
    <div class="person">
      <p class="person__name">Maren Holloway</p>
      <p class="person__role">FOUNDER &amp; CEO</p>
    </div>
    <div class="front-rule front-rule--name"></div>
    <ul class="contact">
      <li>
        <svg class="contact__icon" viewBox="0 0 16 16" aria-hidden="true"><circle cx="8" cy="8" r="8" fill="var(--brand-blue)"/><path d="M5 4.5h2l.6 2-1 .8a5 5 0 0 0 2.1 2.1l.8-1 2 .6v2c0 .5-.4.8-.9.8A6.5 6.5 0 0 1 4.2 5.4c0-.5.3-.9.8-.9z" fill="#fff"/></svg>
        <span class="contact__text">0512340987</span>
      </li>
      <li>
        <svg class="contact__icon" viewBox="0 0 16 16" aria-hidden="true"><circle cx="8" cy="8" r="8" fill="var(--brand-blue)"/><rect x="5.5" y="3.5" width="5" height="9" rx="1" fill="#fff"/><circle cx="8" cy="11" r=".7" fill="var(--brand-blue)"/></svg>
        <span class="contact__text">0176420318</span>
      </li>
      <li>
        <svg class="contact__icon" viewBox="0 0 16 16" aria-hidden="true"><circle cx="8" cy="8" r="8" fill="var(--brand-blue)"/><rect x="4" y="5" width="8" height="6" rx=".8" fill="#fff"/><path d="M4.3 5.4 8 8.3l3.7-2.9" fill="none" stroke="var(--brand-blue)" stroke-width=".9"/></svg>
        <span class="contact__text">care@northvale.com.au</span>
      </li>
      <li>
        <svg class="contact__icon" viewBox="0 0 16 16" aria-hidden="true"><circle cx="8" cy="8" r="8" fill="var(--brand-blue)"/><path d="M8 3.8 3.8 7.6h1.3V12h2.2V9.5h1.4V12h2.2V7.6h1.3z" fill="#fff"/></svg>
        <span class="contact__text">Unit 4, Larkfield, Orin st<br>Canada</span>
      </li>
    </ul>
    <p class="website">www.brightpathsolutions.com</p>
  </section>

</body>
</html>
```